Meridel Hair Studio Needs a new appointment business card

We need a new appointment card for our hair salon.

I Dont want bright out there colours.
I would like it to be neat, clean, easy to read. White, Black, with a hint of colour if needed.

We need
-Logo
-Phone number 47208613
-Mobile Number: 0417306852
Address: Shop 3/214 Calder Road, The Elmgates, Tarrin 4812

BACK SIDE OF CARD
- Appointment Time & Date (White background so we are able to write on it)
(If you are unable to make your appointment please contact us ASAP 47208613)

I also would like the chatterly and Pictorama logo(Find us on Chatterly)(find us on Pictorama)

Target Market(s)

appointment card simple to read. all information for their next appoint For all our clients male and female

Industry/Entity Type

Hairdresser

Contact Information for Business Card

-Logo
-Phone number 47208613

BACK SIDE OF CARD

Font styles to use
Serif
Sans Serif
Script

Requirements
Must have
• White Back ground on backside with appointment deatils so we are able to write information (like appointment time and date)
Nice to have
• Find us on Chatterly
and
pictorama - meridel_hairstudio
Should not have
• BRIGHT COLOURS

```html
<!DOCTYPE html>
<html lang="en">
<head>
<meta charset="utf-8">
<title>Meridel Hair Studio – Business &amp; Appointment Card</title>
<link rel="stylesheet" href="https://fonts.googleapis.com/css2?family=Cinzel:wght@600&family=Libre+Baskerville:wght@700&family=Arimo:wght@400&display=swap">
<style>
  :root {
    --bg: #b9b9b9;
    --card: #ffffff;
    --ink: #111111;
    --ink-soft: #2a2a2a;
    --rule: #555555;
  }
  * { box-sizing: border-box; margin: 0; padding: 0; }
  html, body { width: 1200px; height: 801px; overflow: hidden; }
  body {
    background: var(--bg);
    font-family: "Arimo", Arial, sans-serif;
    color: var(--ink);
    display: flex;
    align-items: center;
    justify-content: center;
    gap: 44px;
  }
  .card {
    position: relative;
    width: 540px;
    height: 310px;
    background: var(--card);
    border-radius: 22px;
    overflow: hidden;
    box-shadow: 0 10px 24px rgba(0,0,0,.25);
  }
  .brand {
    font-family: "Cinzel", Georgia, serif;
    font-weight: 600;
    color: var(--ink);
    display: flex;
    align-items: center;
    gap: 10px;
    letter-spacing: .02em;
    white-space: nowrap;
  }
  .brand-dot {
    width: 14px; height: 14px;
    border: 3px solid var(--ink);
    border-radius: 50%;
    flex: none;
  }

  /* Front */
  .front .tab {
    position: absolute; right: 20px; top: 0;
    width: 34px; height: 26px; background: var(--ink);
  }
  .front .holder {
    position: absolute; right: 62px; top: 30px; text-align: right;
  }
  .holder-name {
    font-family: "Libre Baskerville", Georgia, serif;
    font-weight: 700; font-size: 19px;
  }
  .holder-role { font-size: 12px; color: var(--ink-soft); margin-top: 2px; }
  .front .brand { position: absolute; left: 36px; top: 92px; font-size: 30px; }
  .front .rule {
    position: absolute; left: 36px; right: 62px; top: 150px;
    height: 1px; background: var(--rule);
  }
  .contacts {
    position: absolute; left: 36px; bottom: 28px;
    list-style: none; font-size: 13.5px; line-height: 1.55;
  }
  .contacts li { display: flex; align-items: center; gap: 8px; white-space: nowrap; }
  .contacts svg { width: 11px; height: 11px; flex: none; fill: var(--ink); }
  .social {
    position: absolute; right: 30px; top: 166px;
    display: flex; align-items: center; gap: 6px; font-size: 12.5px;
  }
  .social-mark { width: 10px; height: 10px; background: var(--ink); border-radius: 2px; }
  .front .edge {
    position: absolute; left: 0; right: 0; bottom: 0; height: 8px; background: var(--ink);
  }

  /* Back */
  .back .brand {
    position: absolute; left: 0; right: 0; top: 54px;
    justify-content: center; font-size: 32px;
  }
  .appointment-title {
    position: absolute; left: 0; right: 0; top: 122px;
    text-align: center; font-size: 17px; letter-spacing: .04em;
  }
  .fill-row {
    position: absolute; left: 36px; right: 36px; top: 186px;
    display: flex; gap: 28px; font-size: 15px;
  }
  .fill-field { flex: 1; display: flex; align-items: flex-end; gap: 6px; }
  .fill-line { flex: 1; height: 1px; background: var(--rule); margin-bottom: 4px; }
  .notice-band {
    position: absolute; left: 0; right: 0; bottom: 0; height: 48px;
    background: var(--ink); color: var(--card);
    display: flex; align-items: center; justify-content: center;
    font-size: 13px; letter-spacing: .02em;
  }
</style>
</head>
<body>

  <section class="card front" aria-label="Business card front">
    <div class="tab"></div>
    <div class="holder">
      <div class="holder-name">Adrien Kellow</div>
      <div class="holder-role">Owner</div>
    </div>
    <div class="brand"><span class="brand-dot"></span>Meridel Hair Studio</div>
    <div class="rule"></div>
    <div class="social">meridelhairstudio <span class="social-mark"></span></div>
    <ul class="contacts">
      <li><svg viewBox="0 0 24 24"><path d="M6.6 10.8a15 15 0 0 0 6.6 6.6l2.2-2.2c.3-.3.7-.4 1-.2 1.1.4 2.3.6 3.6.6.6 0 1 .4 1 1V20c0 .6-.4 1-1 1A17 17 0 0 1 3 4c0-.6.4-1 1-1h3.5c.6 0 1 .4 1 1 0 1.3.2 2.5.6 3.6.1.3 0 .7-.2 1z"/></svg>47208613</li>
      <li><svg viewBox="0 0 24 24"><path d="M7 1h10a2 2 0 0 1 2 2v18a2 2 0 0 1-2 2H7a2 2 0 0 1-2-2V3a2 2 0 0 1 2-2zm0 3v14h10V4z"/></svg>0417306852</li>
      <li><svg viewBox="0 0 24 24"><path d="M2 4h20v16H2zm2 2v.5l8 5.5 8-5.5V6z"/></svg>info@meridelhairstudio.com</li>
      <li><svg viewBox="0 0 24 24"><path d="M12 2a7 7 0 0 1 7 7c0 5-7 13-7 13S5 14 5 9a7 7 0 0 1 7-7zm0 4.5a2.5 2.5 0 1 0 0 5 2.5 2.5 0 0 0 0-5z"/></svg>Shop 3/214 Calder Road, The Elmgates, Tarrin 4812</li>
    </ul>
    <div class="edge"></div>
  </section>

  <section class="card back" aria-label="Appointment card back">
    <div class="brand"><span class="brand-dot"></span>Meridel Hair Studio</div>
    <div class="appointment-title">APPOINTMENT</div>
    <div class="fill-row">
      <div class="fill-field">Date: <span class="fill-line"></span></div>
      <div class="fill-field">Time: <span class="fill-line"></span></div>
    </div>
    <div class="notice-band">If you are unable to make your appointment please contact us ASAP 47208613</div>
  </section>

</body>
</html>
```